Beautiful design for wordpress

I need a beautiful, colourful and feminine website. My business is called 'The Moonlit Brook', and I sell crystals, books, CD's, pendulums and other metaphysical items. I also provide Reiki (energy healing).
I want this design to be eye catching and inspire happiness and joy in those who see it. And I would love to see the use of the logo and its colours :)
Please add these on the web design: Home, About, Online store, Blog

• Colourful and playful, must use the logo somewhere, have the words on a menu saying 'Home, Blog, Online store and about' (or similar to those)And the design must stand out!
• grey, brown and other boring colours.

```html
<!DOCTYPE html>
<html lang="en">
<head>
<meta charset="utf-8">
<title>The Moonlit Brook — Crystals &amp; Gifts</title>
<link href="https://fonts.googleapis.com/css2?family=Open+Sans:wght@400;600;700&family=Lato:wght@400;700&family=Alegreya+Sans+SC:wght@800&display=swap" rel="stylesheet">
<style>
  :root {
    --orange: #fcb25b;
    --green: #c2d67a;
    --green-dark: #a9c25d;
    --pink: #fd8181;
    --ink: #1e1e1e;
    --muted: #7a7a7a;
    --footer: #3d3d3d;
    --chip: #4a4a4a;
    --page: #ffffff;
  }
  * { box-sizing: border-box; margin: 0; padding: 0; }
  html, body { width: 1080px; height: 1200px; overflow: hidden; background: var(--page); }
  body { position: relative; font-family: "Open Sans", sans-serif; color: var(--ink); }

  .brand { position: absolute; left: 158px; top: 52px; display: flex; align-items: center; gap: 8px; }
  .brand-dot { width: 18px; height: 18px; border-radius: 50%; background: var(--pink); }
  .brand-name { font-family: "Open Sans", sans-serif; font-weight: 700; font-size: 19px; color: var(--chip); }

  .search { position: absolute; left: 758px; top: 62px; width: 170px; height: 29px; border: 1px solid #dcdcdc; border-radius: 3px; display: flex; align-items: center; justify-content: space-between; padding: 0 8px; }
  .search span { font-size: 11px; font-style: italic; color: #999; }

  .nav { position: absolute; left: 155px; top: 143px; width: 771px; height: 44px; background: var(--orange); display: flex; align-items: center; }
  .nav a { color: #fff; text-decoration: none; font-size: 14.5px; height: 44px; line-height: 44px; }
  .nav .home { background: var(--green); width: 104px; text-align: center; }
  .nav .item { margin-left: 18px; margin-right: 32px; }
  .social { margin-left: auto; margin-right: 22px; display: flex; gap: 9px; }
  .social i { width: 18px; height: 18px; border-radius: 50%; background: #fff; display: block; }

  .hero { position: absolute; left: 155px; top: 187px; width: 771px; height: 374px; background: linear-gradient(110deg, #e9ddd4 0%, #f3efec 40%, #f6f6f6 70%, #eef0f1 100%); }
  .hero-card { position: absolute; left: 459px; top: 85px; width: 281px; height: 193px; background: var(--green); border-radius: 14px; padding: 34px 20px 0 25px; }
  .hero-card h1 { font-family: "Alegreya Sans SC", sans-serif; font-weight: 800; font-size: 25px; color: #fff; letter-spacing: .5px; margin-left: -1px; }
  .hero-card p { font-size: 9px; line-height: 17px; text-align: justify; margin-top: 9px; }
  .dots { position: absolute; left: 369px; top: 345px; display: flex; gap: 4px; }
  .dots i { width: 14px; height: 14px; border-radius: 50%; background: var(--chip); border: 2px solid #fff; display: block; }
  .dots i.on { background: var(--orange); }

  .section-title { position: absolute; left: 155px; top: 573px; font-size: 14.5px; }

  .product { position: absolute; top: 607px; width: 179px; }
  .product .photo { height: 164px; }
  .product .label { margin-top: 4px; height: 40px; display: flex; align-items: center; justify-content: space-between; padding: 0 20px 0 11px; color: #fff; font-size: 14px; }
  .arrow { width: 21px; height: 21px; border-radius: 50%; background: var(--chip); display: flex; align-items: center; justify-content: center; }

  .welcome { position: absolute; left: 155px; top: 840px; width: 771px; text-align: center; }
  .welcome h2 { font-family: "Lato", sans-serif; font-weight: 400; font-size: 19px; }
  .welcome h2 span { color: var(--muted); font-weight: 700; }
  .welcome p { font-family: "Lato", sans-serif; font-size: 9px; line-height: 17px; margin-top: 11px; padding: 0 10px; }

  .reiki { position: absolute; left: 155px; top: 954px; width: 771px; height: 157px; background: var(--orange); }
  .reiki-text { position: absolute; left: 21px; top: 14px; width: 406px; }
  .reiki h3 { font-weight: 400; font-size: 17.5px; color: #fff; }
  .reiki p { font-size: 9px; line-height: 17px; text-align: justify; margin-top: 11px; }
  .reiki .more { display: block; margin-top: 9px; font-size: 8.5px; font-weight: 700; color: #fff; text-decoration: none; }
  .reiki-photo { position: absolute; right: 0; top: 0; width: 300px; height: 157px; background: linear-gradient(90deg, var(--orange) 0%, #e9c3a2 18%, #e8e4e0 55%, #f1f0ee 100%); }

  .footer { position: absolute; left: 0; top: 1144px; width: 1080px; height: 56px; background: var(--footer); border-top: 2px solid var(--green-dark); color: #fff; font-size: 9px; letter-spacing: .3px; }
  .footer .copy { position: absolute; left: 156px; top: 18px; }
  .footer .links { position: absolute; right: 152px; top: 19px; }
  .footer .links span { margin: 0 6px; }
</style>
</head>
<body>
  <header>
    <div class="brand"><i class="brand-dot"></i><span class="brand-name">The Moonlit Brook</span></div>
    <div class="search"><span>Search</span>
      <svg width="14" height="14" viewBox="0 0 14 14"><circle cx="5.5" cy="5.5" r="4" fill="none" stroke="#555" stroke-width="1.6"/><line x1="8.5" y1="8.5" x2="13" y2="13" stroke="#555" stroke-width="2.2" stroke-linecap="round"/></svg>
    </div>
    <nav class="nav">
      <a class="home" href="#">Home</a>
      <a class="item" href="#">About</a>
      <a class="item" href="#">Online store</a>
      <a class="item" href="#">Blog</a>
      <a class="item" href="#">Contact us</a>
      <div class="social"><i></i><i></i><i></i><i></i></div>
    </nav>
  </header>

  <section class="hero" role="img" aria-label="Photo of a Reiki practitioner resting hands on a relaxed client's forehead">
    <div class="hero-card">
      <h1>THE MOONLIT BROOK</h1>
      <p>Lorem ipsum dolor sit amet conse ctetur adipisicing elit, sed do eiusmod tempor incididunt ut labore et dolore magna aliqua. Ut enim ad minim veniam, quis nostrud exercitation ullamco. Lorem ipsum dolor sit amet conse ctetur adipisicing eli.</p>
    </div>
    <div class="dots"><i class="on"></i><i></i><i></i></div>
  </section>

  <h2 class="section-title">Our Products</h2>

  <div class="product" style="left:155px">
    <div class="photo" role="img" aria-label="Photo of a clear quartz crystal cluster" style="background:linear-gradient(160deg,#8d9a5a,#e6e2e4 40%,#cfc6cc 70%,#3b3a30)"></div>
    <div class="label" style="background:var(--orange)">Crystals<span class="arrow"><svg width="8" height="10" viewBox="0 0 8 10"><path d="M2 1l4 4-4 4" fill="none" stroke="#fff" stroke-width="2"/></svg></span></div>
  </div>
  <div class="product" style="left:351px">
    <div class="photo" role="img" aria-label="Photo of colourful hardback books lined up" style="background:linear-gradient(135deg,#f2f2f2,#e0a04a 30%,#8ab04a 50%,#c94a4a 70%,#f4f4f4)"></div>
    <div class="label" style="background:var(--green)">Books<span class="arrow"><svg width="8" height="10" viewBox="0 0 8 10"><path d="M2 1l4 4-4 4" fill="none" stroke="#fff" stroke-width="2"/></svg></span></div>
  </div>
  <div class="product" style="left:549px">
    <div class="photo" role="img" aria-label="Photo of a stack of CD cases and a disc" style="background:linear-gradient(160deg,#f1f1f3,#9a9aa4 45%,#3e3f4c 80%,#2c2d38)"></div>
    <div class="label" style="background:var(--orange)">CD's<span class="arrow"><svg width="8" height="10" viewBox="0 0 8 10"><path d="M2 1l4 4-4 4" fill="none" stroke="#fff" stroke-width="2"/></svg></span></div>
  </div>
  <div class="product" style="left:747px">
    <div class="photo" role="img" aria-label="Photo of crystal pendulums hanging over wood" style="background:linear-gradient(180deg,#e0b47d,#d7a56a 60%,#c89358)"></div>
    <div class="label" style="background:var(--pink)">Pendulums<span class="arrow"><svg width="8" height="10" viewBox="0 0 8 10"><path d="M2 1l4 4-4 4" fill="none" stroke="#fff" stroke-width="2"/></svg></span></div>
  </div>

  <section class="welcome">
    <h2>Welcome To <span>The Moonlit Brook</span></h2>
    <p>Verolore magnam aliquam quaerat voluptatem. Cerut enim ad minimeniam, quis nostrum exercitationem ullorporis suscipit. Verolore magnam aliquam quaerat voluptatem. Cerut enim ad minimeniam, quis nostrum exercitationem ullorporis suscipit. Verolore magnam aliquam quaerat voluptatem. Cerut enim ad minimeniam, quis nostrum exercitationem ullorporis suscipit. Verolore magnam aliquam quaerat voluptatem. Cerut enim ad minimeniam, quis nostrum exercitationem ullorporis suscipit.</p>
  </section>

  <section class="reiki">
    <div class="reiki-text">
      <h3>Reiki (energy healing)</h3>
      <p>Beciegast nveriti vitaesaert asety kertya aset aplicaboserde nerakertyu erauas vitaesa ertyasnemo fasera iptaiades kertyaser daesraeds. Servolernatur aut oditaueras onsequuntur magni dolores eo qui ratione voluptate msequi nesciunt neque porro quisquam estui dolorem ipsum, quia dolor.</p>
      <a class="more" href="#">Read More</a>
    </div>
    <div class="reiki-photo" role="img" aria-label="Photo of a therapist giving a Reiki treatment in a bright room"></div>
  </section>

  <footer class="footer">
    <div class="copy">©2014 2014 &nbsp;THE MOONLIT BROOK, ALL RIGHTS RESERVED.</div>
    <div class="links">HOME<span>|</span> ABOUT<span>|</span> ONLINE STORE<span>|</span>BLOG<span>|</span>CONTACT US</div>
  </footer>
</body>
</html>
```